ZOR Clinic

We are a telemedicine based HIV treatment, prevention and hep c clinic looking to help make our online presence known.

Target Market(s)

Future patients. We want to this be informative and have stock images of all different types of people

Industry/Entity Type

Medical

Coding

Coded - Design and coding required

Requirements
Must have
• A Home Page, A page on PrEP, HIV treatment and Hep C. A box in the corner that says book now and a contact us page.

```html
<!DOCTYPE html>
<html lang="en">
<head>
<meta charset="utf-8">
<title>ZOR Clinic — Online HIV, PrEP and Hep C Care</title>
<link href="https://fonts.googleapis.com/css2?family=Inter:wght@400;500;600;700;800&family=Playfair+Display:ital,wght@1,500&display=swap" rel="stylesheet">
<style>
:root{
  --navy:#0c2340;
  --blue:#0a5bb0;
  --blue-dark:#073f85;
  --green:#7dc242;
  --green-dark:#5aa02c;
  --cream:#f8f5ef;
  --white:#ffffff;
  --ink:#1b2230;
}
*{box-sizing:border-box;margin:0;padding:0}
html,body{width:1200px;height:3161px;overflow:hidden}
body{font-family:"Inter",Arial,sans-serif;color:var(--ink);background:var(--cream);position:relative}
.abs{position:absolute}
.script{font-family:"Playfair Display",Georgia,serif;font-style:italic;font-weight:500;color:var(--green)}
.swoosh{position:absolute;display:block}

.topbar{left:0;top:0;width:1200px;height:22px;background:var(--blue);display:flex;justify-content:center;gap:30px;align-items:center;color:#fff;font-size:9px}
.topbar span::before{content:"";display:inline-block;width:8px;height:8px;border-radius:2px;background:var(--green);margin-right:4px;vertical-align:-1px}

.logo{left:22px;top:44px;display:flex;align-items:center;gap:10px;font-weight:800;font-size:28px;color:var(--navy)}
.logo i{width:26px;height:26px;background:var(--green);border-radius:50%;display:block}
.nav a{position:absolute;top:58px;font-size:14px;color:var(--navy);text-decoration:none}
.nav a.active{font-weight:700}
.nav a.active::after{content:"";position:absolute;left:-4px;right:-4px;top:22px;height:3px;border-radius:3px;background:var(--blue)}
.book-now{left:968px;top:48px;width:117px;height:34px;background:var(--green);color:#fff;font-weight:700;font-size:14px;display:flex;align-items:center;justify-content:center}

.hero-title{left:58px;top:172px;font-size:61px;font-weight:700;color:var(--navy);letter-spacing:-.5px}
.hero-script{left:62px;top:240px;font-size:76px}
.hero-sub{left:58px;top:378px;font-size:28px;line-height:44px;color:var(--navy)}
.btn{position:absolute;display:flex;align-items:center;justify-content:center;font-weight:700;text-decoration:none}
.btn-primary{background:var(--blue);color:#fff}
.btn-outline{border:2px solid #b9de94;color:var(--green);background:transparent}
.hero-art{left:589px;top:130px;width:580px;height:460px;border-radius:50%;background:linear-gradient(135deg,#8fcb55 0%,#c9b9a4 35%,#3a4a66 62%,#0a66c0 100%)}

.stats{left:0;top:640px;width:1200px;height:191px;background:var(--navy)}
.stat-num{position:absolute;top:52px;font-size:33px;font-weight:600;color:#fff}
.stat-label{position:absolute;top:96px;font-size:15px;line-height:22px;color:#fff}
.stat-icon{position:absolute;top:55px}
.stat-div{position:absolute;top:55px;width:1px;height:82px;background:#3a5070}

.section-title{position:absolute;left:0;width:1200px;text-align:center;font-weight:800}
.services-title{top:900px;font-size:58px;color:var(--navy)}
.card{position:absolute;top:1037px;width:340px;height:319px;background:#fff;text-align:center}
.card svg{position:absolute;left:117px;top:33px}
.card h3{position:absolute;top:152px;left:0;width:100%;font-size:31px;font-weight:700;color:var(--navy)}
.card p{position:absolute;top:199px;left:40px;right:40px;font-size:11.5px;line-height:20px;color:var(--ink)}
.card .learn{position:absolute;top:254px;left:112px;width:116px;height:31px;border:1px solid var(--green);color:var(--green);font-size:12.5px;font-weight:600;display:flex;align-items:center;justify-content:center}

.steps{left:0;top:1446px;width:1200px;height:502px;background:var(--navy)}
.steps-title{top:70px;font-size:40px;color:#fff;font-weight:700}
.step{position:absolute;width:340px;text-align:center;color:#fff}
.step .badge{position:absolute;top:178px;left:158px;width:24px;height:24px;border-radius:50%;background:#fff;color:var(--navy);font-size:10px;font-weight:700;display:flex;align-items:center;justify-content:center}
.step svg{position:absolute;left:116px;top:216px}
.step h3{position:absolute;top:340px;left:0;width:100%;font-size:26px;font-weight:700}
.step p{position:absolute;top:383px;left:30px;right:30px;font-size:11.5px;line-height:20px}

.real{left:0;top:1948px;width:1200px;height:373px;background:linear-gradient(90deg,#2d2a27 0%,#4b4640 40%,#8c8174 62%,#6e6459 100%)}
.real-title{left:54px;top:70px;font-size:42px;font-weight:700;color:#fff}
.real-text{left:62px;top:173px;width:500px;text-align:center;color:#fff;font-size:11.5px;line-height:20px}
.feature{position:absolute;top:222px;width:120px;text-align:center;color:#fff;font-size:11.5px;line-height:19px}
.feature svg{display:block;margin:0 auto 6px}

.ready-art{left:80px;top:2400px;width:546px;height:430px;border-radius:50%;background:linear-gradient(135deg,#8fcb55 0%,#b9b4aa 30%,#5b6d88 60%,#0a5bb0 100%)}
.ready-title{left:640px;width:505px;text-align:center;position:absolute}
.ready-h{top:2440px;font-size:48px;font-weight:700;color:var(--navy)}
.ready-s{top:2500px;font-size:48px}
.ready-p{top:2612px;font-size:21.5px;line-height:30px;color:var(--navy)}

.footer{left:0;top:2896px;width:1200px;height:265px;background:var(--navy);color:#fff}
.f-logo{left:81px;top:44px;font-size:18px;font-weight:800;display:flex;gap:8px;align-items:center}
.f-logo i{width:16px;height:16px;border-radius:50%;background:var(--green)}
.f-tag{left:81px;top:102px;font-size:11.5px;line-height:19px}
.social{position:absolute;top:148px;width:24px;height:24px;border-radius:50%;background:#fff}
.f-col{position:absolute;top:44px}
.f-col h4{font-size:22px;font-weight:700;margin-bottom:8px}
.f-col li{list-style:none;font-size:11.5px;line-height:22px}
.f-col li::before{content:"+";color:var(--green);font-weight:800;margin-right:7px}
.f-div{position:absolute;top:44px;width:1px;height:120px;background:#2e4566}
.f-line{left:81px;top:208px;width:1038px;height:1px;background:#2e4566}
.f-copy{left:81px;top:225px;font-size:11px}
.f-legal{left:783px;top:225px;font-size:11px;display:flex;gap:10px}
.f-legal span+span::before{content:"|";margin-right:10px}
</style>
</head>
<body>

<div class="abs topbar">
  <span>100% Online &amp; Private</span><span>HIPAA Secure</span><span>Board-Certified Clinicians</span><span>Insurance &amp; Affordable Options</span>
</div>

<header>
  <div class="abs logo"><i></i>ZOR Clinic</div>
  <nav class="nav">
    <a class="active" style="left:432px">Home</a>
    <a style="left:500px">Care</a>
    <a style="left:561px">How It Works</a>
    <a style="left:675px">About Us</a>
    <a style="left:763px">Resources</a>
    <a style="left:860px">For Partners</a>
  </nav>
  <div class="abs book-now">+ BOOK NOW</div>
</header>

<section class="hero">
  <h1 class="abs hero-title">Care that meets you</h1>
  <div class="abs script hero-script">where you are.</div>
  <svg class="swoosh" style="left:58px;top:340px" width="312" height="28" viewBox="0 0 312 28"><path d="M2 24 Q150 -4 310 6 Q160 6 2 24Z" fill="var(--blue)"/></svg>
  <p class="abs hero-sub">Private, inclusive HIV, PrEP and<br>Hep C care — 100% online.</p>
  <a class="btn btn-primary" style="left:58px;top:491px;width:235px;height:55px;font-size:18px">+ Book a private visit</a>
  <a class="btn btn-outline" style="left:310px;top:491px;width:183px;height:55px;font-size:18px">Explore care →</a>
  <div class="abs hero-art" role="img" aria-label="Green and blue swoosh framing arched portraits of three diverse patients, with a green plus emblem"></div>
</section>

<section class="abs stats">
  <svg class="stat-icon" style="left:53px" width="72" height="78" viewBox="0 0 72 78" fill="none" stroke="var(--green)" stroke-width="3"><circle cx="36" cy="16" r="14"/><path d="M36 9v14M29 16h14"/><circle cx="14" cy="44" r="7"/><circle cx="36" cy="44" r="7"/><circle cx="58" cy="44" r="7"/><path d="M2 76v-8a12 12 0 0 1 24 0v8M24 76v-8a12 12 0 0 1 24 0v8M46 76v-8a12 12 0 0 1 24 0v8"/></svg>
  <div class="stat-num" style="left:145px">25,000+</div>
  <div class="stat-label" style="left:145px">Patients served<br>across the U.S.</div>
  <div class="stat-div" style="left:315px"></div>
  <svg class="stat-icon" style="left:356px" width="66" height="80" viewBox="0 0 66 80" fill="none" stroke="var(--green)" stroke-width="3"><path d="M12 2h36l14 14v62H12Z"/><path d="M22 18h20M22 28h30"/><path d="M2 38h20l6 6h26v34H2Z"/><rect x="20" y="56" width="18" height="14"/><path d="M23 56v-6a6 6 0 0 1 12 0v6"/></svg>
  <div class="stat-num" style="left:443px">100%</div>
  <div class="stat-label" style="left:443px">Private &amp;<br>confidential</div>
  <div class="stat-div" style="left:569px"></div>
  <svg class="stat-icon" style="left:611px" width="78" height="78" viewBox="0 0 78 78" fill="none" stroke="var(--green)" stroke-width="3"><circle cx="39" cy="41" r="34"/><circle cx="39" cy="41" r="22"/><path d="M39 28v13l9 7"/><path d="M30 2h18"/></svg>
  <div class="stat-num" style="left:709px">98%</div>
  <div class="stat-label" style="left:709px">Patient<br>satisfaction rate</div>
  <div class="stat-div" style="left:863px"></div>
  <svg class="stat-icon" style="left:903px" width="72" height="78" viewBox="0 0 72 78" fill="none" stroke="var(--green)" stroke-width="3"><path d="M36 2l4 8 9 1-6 6 2 9-9-4-9 4 2-9-6-6 9-1Z"/><path d="M12 14l2 5 6 1-4 4 1 6-5-3-5 3 1-6-4-4 6-1Z"/><path d="M60 14l2 5 6 1-4 4 1 6-5-3-5 3 1-6-4-4 6-1Z"/><rect x="4" y="44" width="12" height="30"/><path d="M16 48l12-14 4 2-2 12h18a5 5 0 0 1 0 10h-2a5 5 0 0 1 0 10h-4a4 4 0 0 1 0 6H16"/></svg>
  <div class="stat-num" style="left:995px">24–48 hrs</div>
  <div class="stat-label" style="left:995px">Average time to get<br>started</div>
</section>

<section class="services">
  <h2 class="section-title services-title">SERVICES</h2>
  <svg class="swoosh" style="left:490px;top:978px" width="220" height="24" viewBox="0 0 220 24"><path d="M2 22 Q110 -6 218 6 Q110 6 2 22Z" fill="var(--blue)"/></svg>

  <article class="card" style="left:53px">
    <svg width="106" height="106" viewBox="0 0 106 106" fill="none"><path d="M53 3a50 50 0 0 1 0 100" stroke="var(--green)" stroke-width="3"/><path d="M53 103a50 50 0 0 1 0-100" stroke="var(--blue)" stroke-width="3"/><g stroke="var(--navy)" stroke-width="2.5"><path d="M30 72h46M32 66c8 0 16 2 21 6 5-4 13-6 21-6"/><path d="M36 48h34a17 17 0 0 1-34 0Z"/><circle cx="53" cy="40" r="6"/></g></svg>
    <h3>PrEP</h3>
    <p>PrEP is a safe, effective way to help protect you from HIV. We make it simple—online.</p>
    <div class="learn">Learn more →</div>
  </article>
  <article class="card" style="left:430px">
    <svg width="106" height="106" viewBox="0 0 106 106" fill="none"><path d="M53 3a50 50 0 0 1 0 100" stroke="var(--green)" stroke-width="3"/><path d="M53 103a50 50 0 0 1 0-100" stroke="var(--blue)" stroke-width="3"/><g stroke="var(--navy)" stroke-width="2.5"><path d="M53 22l24 8v18c0 16-10 26-24 32-14-6-24-16-24-32V30Z"/><circle cx="48" cy="48" r="7"/><circle cx="58" cy="54" r="7"/></g></svg>
    <h3>HIV Treatment</h3>
    <p>Evidence-based care that supports your health and your life—online.</p>
    <div class="learn">Learn more →</div>
  </article>
  <article class="card" style="left:806px">
    <svg width="106" height="106" viewBox="0 0 106 106" fill="none"><path d="M53 3a50 50 0 0 1 0 100" stroke="var(--green)" stroke-width="3"/><path d="M53 103a50 50 0 0 1 0-100" stroke="var(--blue)" stroke-width="3"/><g stroke="var(--navy)" stroke-width="2.5"><path d="M53 58c-12-8-18-14-18-22a9 9 0 0 1 18-3 9 9 0 0 1 18 3c0 8-6 14-18 22Z"/><path d="M28 44v18l14 14M78 44v18L64 76"/></g></svg>
    <h3>Hep C Care</h3>
    <p>Cure is possible. Our team makes Hep C treatment convenient and accessible.</p>
    <div class="learn">Learn more →</div>
  </article>
</section>

<section class="abs steps">
  <h2 class="section-title steps-title">Simple steps. <span class="script" style="font-size:42px">Real support.</span></h2>
  <svg class="swoosh" style="left:490px;top:136px" width="220" height="24" viewBox="0 0 220 24"><path d="M2 22 Q110 -6 218 6 Q110 6 2 22Z" fill="var(--blue)"/></svg>
  <svg class="abs" style="left:0;top:268px" width="1200" height="2"><path d="M290 1H530M667 1H907" stroke="#3a5070" stroke-width="1.5" stroke-dasharray="2 4"/></svg>

  <div class="step" style="left:52px">
    <div class="badge">01</div>
    <svg width="108" height="108" viewBox="0 0 108 108" fill="none"><path d="M54 3a51 51 0 0 1 0 102" stroke="var(--green)" stroke-width="3"/><path d="M54 105a51 51 0 0 1 0-102" stroke="var(--blue)" stroke-width="3"/><g stroke="#fff" stroke-width="2.5"><rect x="30" y="36" width="40" height="28"/><path d="M44 64v8h12v-8M40 72h20"/><rect x="56" y="30" width="22" height="20" fill="var(--navy)"/><path d="M61 41l4 4 8-8"/></g></svg>
    <h3>Book online</h3>
    <p>Choose a time that works for you and answer a few quick questions.</p>
  </div>
  <div class="step" style="left:429px">
    <div class="badge">02</div>
    <svg width="108" height="108" viewBox="0 0 108 108" fill="none"><path d="M54 3a51 51 0 0 1 0 102" stroke="var(--green)" stroke-width="3"/><path d="M54 105a51 51 0 0 1 0-102" stroke="var(--blue)" stroke-width="3"/><g stroke="#fff" stroke-width="2.5"><rect x="28" y="32" width="44" height="32"/><circle cx="42" cy="46" r="5"/><path d="M34 62a8 8 0 0 1 16 0"/><path d="M54 40h12M54 46h10"/><circle cx="70" cy="62" r="6"/><path d="M60 80a10 10 0 0 1 20 0Z"/></g></svg>
    <h3>Meet with your provider</h3>
    <p>Connect from anywhere. Compassionate care, judgment-free.</p>
  </div>
  <div class="step" style="left:805px">
    <div class="badge">03</div>
    <svg width="108" height="108" viewBox="0 0 108 108" fill="none"><path d="M54 3a51 51 0 0 1 0 102" stroke="var(--green)" stroke-width="3"/><path d="M54 105a51 51 0 0 1 0-102" stroke="var(--blue)" stroke-width="3"/><g stroke="#fff" stroke-width="2.5"><rect x="36" y="32" width="36" height="26"/><path d="M36 40h36M50 46h8M54 42v8"/><path d="M26 70l12-6h14l8 4h14l6-6"/><path d="M26 78h30l20-10"/></g></svg>
    <h3>Get your meds, your way</h3>
    <p>Medications delivered discreetly to your door with ongoing support built in.</p>
  </div>
</section>

<section class="abs real" role="img" aria-label="Young man relaxing on a sofa at home, smiling at his phone">
  <h2 class="abs real-title">Care built around <span class="script" style="font-size:44px">Real Life.</span></h2>
  <svg class="swoosh" style="left:165px;top:124px" width="220" height="22" viewBox="0 0 220 22"><path d="M2 20 Q110 -6 218 6 Q110 6 2 20Z" fill="var(--blue)"/></svg>
  <p class="abs real-text">We're here for the moments in between the big ones. Ongoing care, real conversations, and support that fits your life—so you can focus on what matters most.</p>
  <div class="feature" style="left:73px"><svg width="32" height="32" viewBox="0 0 32 32" fill="none" stroke="var(--green)" stroke-width="2"><circle cx="16" cy="10" r="6"/><path d="M5 30a11 11 0 0 1 22 0"/></svg>Your privacy<br>comes first</div>
  <div class="feature" style="left:189px"><svg width="32" height="32" viewBox="0 0 32 32" fill="none" stroke="var(--green)" stroke-width="2"><circle cx="10" cy="10" r="4"/><circle cx="22" cy="10" r="4"/><path d="M3 26a7 7 0 0 1 14 0M15 26a7 7 0 0 1 14 0"/></svg>Inclusive care<br>for every body</div>
  <div class="feature" style="left:313px"><svg width="32" height="32" viewBox="0 0 32 32" fill="none" stroke="var(--green)" stroke-width="2"><circle cx="16" cy="16" r="13"/><path d="M10 16l4 4 8-8"/></svg>Judgment-free<br>and affirming</div>
  <div class="feature" style="left:430px"><svg width="32" height="32" viewBox="0 0 32 32" fill="none" stroke="var(--green)" stroke-width="2"><path d="M16 28C6 21 2 16 2 10a7 7 0 0 1 14-2 7 7 0 0 1 14 2c0 6-4 11-14 18Z"/></svg>Support that<br>never quits</div>
</section>

<section class="ready">
  <div class="abs ready-art" role="img" aria-label="Green and blue swoosh framing a photo of a smiling man in a cap on a couch using his phone, with a green plus emblem"></div>
  <h2 class="ready-title ready-h">Ready when</h2>
  <div class="ready-title script ready-s">You are.</div>
  <svg class="swoosh" style="left:767px;top:2570px" width="252" height="24" viewBox="0 0 252 24"><path d="M2 22 Q126 -6 250 6 Q126 6 2 22Z" fill="var(--blue)"/></svg>
  <p class="ready-title ready-p">Book your private visit today and take the next step toward better health.</p>
  <a class="btn btn-primary" style="left:697px;top:2699px;width:212px;height:50px;font-size:17px">+ Book a private visit</a>
  <a class="btn btn-outline" style="left:925px;top:2699px;width:163px;height:50px;font-size:17px">Explore care →</a>
</section>

<footer class="abs footer">
  <div class="abs f-logo"><i></i>ZOR Clinic</div>
  <p class="abs f-tag">Private, inclusive HIV, PrEP and<br>Hep C care—100% online.</p>
  <span class="social" style="left:81px"></span><span class="social" style="left:115px"></span><span class="social" style="left:149px"></span><span class="social" style="left:183px"></span>
  <div class="f-div" style="left:301px"></div>
  <div class="f-col" style="left:356px"><h4>Care</h4><ul><li>PrEP</li><li>HIV Treatment</li><li>Hep C Care</li></ul></div>
  <div class="f-div" style="left:502px"></div>
  <div class="f-col" style="left:557px"><h4>About</h4><ul><li>About Us</li><li>Our Clinicians</li><li>Careers</li><li>News</li></ul></div>
  <div class="f-div" style="left:701px"></div>
  <div class="f-col" style="left:755px"><h4>Resources</h4><ul><li>Patient Resources</li><li>FAQs</li><li>Blog</li><li>Financial Assistance</li></ul></div>
  <div class="f-div" style="left:933px"></div>
  <div class="f-col" style="left:988px"><h4>For Partners</h4><ul><li>Community Partners</li><li>Referring Providers</li><li>Employers</li></ul></div>
  <div class="abs f-line"></div>
  <p class="abs f-copy">© 2025 ZOR Clinic. All rights reserved.</p>
  <p class="abs f-legal"><span>Privacy Policy</span><span>Terms of Use</span><span>Notice of Privacy Practices</span></p>
</footer>

</body>
</html>
```